Bright Pathway! A website showcasing who I am as a person

Bright Pathway started out as idea for me to better myself as a person and work on small projects that would help me grow as a person. Now I want to build a website showcasing "Bright Pathway." I want the website to showcase who I am and how I have grown both professionally and personally. I can build the raw code of the website on my own but I am not really much of a designer. I am looking for a design where I can write and post blogs, articles and share my thoughts. A little about myself and the ideas and interests that I want to share
What is Bright Pathway
Who I am
Background - Professional
Brand Marketing
Email Automation
Hiking
Rock Climbing
Traveling
Exercising and Transformation
"Personal Thoughts"
Hopefully this is enough information to get people started on some designs.
Work
3 page

```html
<!DOCTYPE html>
<html lang="en">
<head>
<meta charset="utf-8">
<title>Bright Pathway</title>
<link rel="stylesheet" href="https://fonts.googleapis.com/css2?family=Open+Sans:ital,wght@0,400;0,600;0,700;1,400;1,700&display=swap">
<style>
:root{
  --teal:#2aa0bf;
  --teal-dark:#1f8aa6;
  --ink:#222;
  --text:#555;
  --muted:#888;
  --pale:#f3f3f3;
  --line:#dedede;
  --white:#fff;
  --footer:#232323;
}
*{box-sizing:border-box;margin:0;padding:0}
html,body{width:1200px;height:4523px;overflow:hidden}
body{font-family:"Open Sans",Arial,sans-serif;color:var(--text);background:var(--white);position:relative}
section,header,footer{position:absolute;left:0;width:1200px}
.abs{position:absolute}
.center{left:0;width:1200px;text-align:center}
.eyebrow{font-size:15px;letter-spacing:4px;color:var(--teal);text-transform:uppercase}
.heading{font-size:36px;letter-spacing:1px;color:var(--ink);text-transform:uppercase;font-weight:400}
.lead{font-size:17px;line-height:28px;color:var(--muted)}

/* hero */
.hero{top:0;height:497px}
.hero-photo{position:absolute;inset:0;background:linear-gradient(100deg,#6f6f6c 0%,#9a9791 35%,#c9c4bb 60%,#8a857c 100%)}
.hero-shade{position:absolute;inset:0;background:rgba(20,20,20,.35)}
.logo{left:60px;top:14px;font-size:38px;font-weight:700;color:var(--white);letter-spacing:1px;text-transform:uppercase}
.nav-rule{left:60px;top:75px;width:1080px;height:1px;background:rgba(255,255,255,.35)}
.nav{right:70px;top:26px;display:flex;gap:50px;font-size:15px;color:rgba(255,255,255,.85)}
.nav .active{color:var(--white);font-weight:600}
.hero-hello{top:216px;font-size:26px;color:var(--white)}
.hero-title{top:246px;font-size:42px;font-weight:600;color:var(--white)}
.btn{display:inline-block;background:var(--teal);color:var(--white);font-weight:600;text-align:center}
.hero-btn{left:527px;top:326px;width:146px;height:36px;line-height:36px;font-size:15px}

/* about */
.about{top:497px;height:754px;background:var(--pale)}
.profile-card{left:60px;top:233px;width:410px;height:461px;background:var(--white);box-shadow:0 1px 3px rgba(0,0,0,.12)}
.profile-photo{height:385px;background:radial-gradient(circle at 50% 45%,#5b8fb0 0%,#3e6f92 60%,#2d5470 100%)}
.profile-name{position:absolute;left:22px;top:394px;font-size:26px;color:var(--ink)}
.profile-sub{position:absolute;left:22px;top:430px;font-size:14px;color:var(--muted)}
.about-text{left:527px;top:250px;width:640px;font-size:17px;line-height:21px;color:var(--muted)}
.about-text p+p{margin-top:21px}
.about-btn{left:527px;top:631px;width:218px;height:51px;line-height:51px;font-size:19px;letter-spacing:1px;box-shadow:0 3px 0 var(--teal-dark)}

/* skills */
.skills{top:1251px;height:462px;background:var(--white)}
.bar{top:169px;width:26px;height:229px;background:#ececec}
.bar span{position:absolute;left:0;bottom:0;width:100%;background:var(--teal)}
.bar-label{top:412px;width:120px;margin-left:-47px;text-align:center;font-size:13px;font-weight:700;color:var(--ink)}

/* works */
.works{top:1713px;height:880px;background:var(--pale)}
.filters{top:212px;left:180px;display:flex;gap:40px;font-size:19px;color:var(--ink);align-items:center}
.filters .on{background:var(--teal);color:var(--white);padding:6px 30px}
.tile{background:#ccc}

/* testimonial */
.testimonial{top:2593px;height:531px;background:var(--white)}
.testi-title{top:50px;font-size:36px;color:var(--ink)}
.avatar{left:531px;top:133px;width:138px;height:138px;border-radius:50%;background:radial-gradient(circle,#a7b9c4,#6f8896);border:4px solid var(--white);box-shadow:0 0 0 2px var(--line)}
.quote{top:286px;left:150px;width:900px;text-align:center;font-size:26px;line-height:42px;font-style:italic;color:#999}
.quote b{font-size:40px;color:#bbb;font-weight:400}
.quote-by{top:382px;font-size:34px;font-style:italic;font-weight:700;color:#666}
.dots{top:467px;left:0;width:1200px;display:flex;justify-content:center;gap:16px}
.dots i{width:9px;height:9px;border-radius:50%;background:#cfe6ee}
.dots i.on{background:var(--teal)}

/* blog */
.blog{top:3124px;height:723px}
.blog-bg{position:absolute;inset:0;background:linear-gradient(120deg,#3fa9c6 0%,#2a97b7 50%,#4bb0cb 100%)}
.blog .eyebrow{color:rgba(255,255,255,.85)}
.blog .heading{color:var(--white)}
.card{top:153px;width:340px;height:468px;background:var(--white);box-shadow:0 2px 6px rgba(0,0,0,.15)}
.card-photo{height:190px}
.card-title{position:absolute;left:28px;top:222px;font-size:24px;color:var(--ink)}
.card-text{position:absolute;left:28px;top:266px;width:290px;font-size:13px;line-height:22px;color:var(--muted)}
.card-more{position:absolute;left:28px;top:415px;font-size:14px;font-weight:700;color:var(--teal)}
.card-count{position:absolute;right:28px;top:413px;font-size:14px;color:var(--muted);display:flex;gap:8px;align-items:center}

/* contact */
.contact{top:3847px;height:483px;background:var(--white)}
.contact-title{left:64px;top:38px;font-size:36px;color:var(--ink);text-transform:uppercase}
.field{border:1px solid var(--line);background:#f7f7f7;font-size:14px;color:#666;padding:16px 14px}
.submit{left:323px;top:392px;width:202px;height:45px;line-height:45px;font-size:22px}
.info-label{display:inline-flex;align-items:center;gap:10px;border:1px solid var(--line);padding:4px 12px;font-size:17px;font-weight:700;color:var(--ink)}
.info-text{font-size:16px;line-height:26px;color:#666}

/* footer */
.footer{top:4330px;height:193px;background:var(--footer)}
.foot-nav{top:40px;left:0;width:1200px;display:flex;justify-content:center;gap:48px;font-size:16px;color:#ddd}
.socials{top:86px;left:0;width:1200px;display:flex;justify-content:center;gap:22px}
.socials i{width:14px;height:14px;border-radius:50%;background:var(--teal)}
.copy{top:124px;font-size:15px;color:#bbb}
</style>
</head>
<body>

<header class="hero">
  <div class="hero-photo" role="img" aria-label="Photo of a bright desk workspace with a computer monitor and keyboard"></div>
  <div class="hero-shade"></div>
  <div class="abs logo">Bright Pathway</div>
  <nav class="abs nav"><span class="active">Home</span><span>Who I am</span><span>Gallery</span><span>Blog</span><span>Contact</span></nav>
  <div class="abs nav-rule"></div>
  <p class="abs center hero-hello">Hello, I'm Sam Rivers</p>
  <h1 class="abs center hero-title">Web Designer &amp; Developer!</h1>
  <a class="abs btn hero-btn">See My Work</a>
</header>

<section class="about">
  <p class="abs center eyebrow" style="top:44px">About</p>
  <h2 class="abs center heading" style="top:64px">Introduction</h2>
  <p class="abs lead" style="left:190px;top:132px;width:820px;text-align:center">Morbi accumsan ipsum velit sodales tellus odio tincidunt auctor ornare sed mauris vitae erat consequat auctor eu in elit class aptent taciti sociosqu ad litora torquent conubia nostra.</p>
  <div class="abs profile-card">
    <div class="profile-photo" role="img" aria-label="Portrait photo of the site owner"></div>
    <div class="profile-name">Leo Marsh</div>
    <div class="profile-sub">Personal Details</div>
  </div>
  <div class="abs about-text">
    <p>Ex id proident ipsum non laborum ut sunt incididunt. Deserunt id ullamco quis in nostrud occaecat ullamco nostrud exercitation nostrud laborum no strud adipisicing cillum. Fugiat magna proident esse laborum nisi culpa id consectetur elit.</p>
    <p>Ex id proident ipsum non laborum ut sunt incididunt. Deserunt id ullamco quis in nostrud occaecat ullamco nostrud exercitation nostrud laborum no strud adipisicing cillum. Fugiat magna proident esse laborum nisi culpa id consectetur elit. Ex id proident ipsum non laborum ut sunt incididunt. Des erunt id ullamco quis in nostrud occaecat ullamco nostrud exercitation nostrud laborum nostrud adipisicing cillum. Fugiat magna proident esse laborum nisi culpa id consectetur elit.</p>
  </div>
  <a class="abs btn about-btn">LEARN MORE</a>
</section>

<section class="skills">
  <p class="abs center eyebrow" style="top:48px">Skills</p>
  <h2 class="abs center heading" style="top:68px">My Professions</h2>
  <div class="abs bar" style="left:228px"><span style="height:100%"></span></div>
  <div class="abs bar" style="left:328px"><span style="height:61%"></span></div>
  <div class="abs bar" style="left:418px"><span style="height:90%"></span></div>
  <div class="abs bar" style="left:512px"><span style="height:50%"></span></div>
  <div class="abs bar" style="left:614px"><span style="height:41%"></span></div>
  <div class="abs bar" style="left:708px"><span style="height:81%"></span></div>
  <div class="abs bar" style="left:804px"><span style="height:100%"></span></div>
  <div class="abs bar" style="left:904px"><span style="height:50%"></span></div>
  <div class="abs bar-label" style="left:228px">BRANDING</div>
  <div class="abs bar-label" style="left:328px">EMAIL</div>
  <div class="abs bar-label" style="left:418px">DESIGN</div>
  <div class="abs bar-label" style="left:512px">WRITING</div>
  <div class="abs bar-label" style="left:614px">HIKING</div>
  <div class="abs bar-label" style="left:708px">CLIMBING</div>
  <div class="abs bar-label" style="left:804px">TRAVEL</div>
  <div class="abs bar-label" style="left:904px">FITNESS</div>
</section>

<section class="works">
  <p class="abs center eyebrow" style="top:38px">Works</p>
  <h2 class="abs center heading" style="top:70px">Recent Projects</h2>
  <p class="abs lead" style="left:190px;top:128px;width:820px;text-align:center">Morbi accumsan ipsum velit sodales tellus odio tincidunt auctor ornare sed mauris vitae erat consequat auctor eu in elit class aptent taciti sociosqu ad litora torquent conubia nostra.</p>
  <div class="abs filters"><span class="on">All</span><span>Hiking</span><span>Rock Climbing</span><span>Traveling</span><span>Exercising</span><span>Transformation</span></div>
  <div class="abs tile" style="left:60px;top:277px;width:251px;height:362px;background:linear-gradient(160deg,#e9eaec,#c9c3b8 70%,#9c7d5c)" role="img" aria-label="Photo of a keyboard and notebooks on a white desk"></div>
  <div class="abs tile" style="left:60px;top:666px;width:251px;height:145px;background:linear-gradient(120deg,#d9a240,#c07b2a 60%,#7a6a5a)" role="img" aria-label="Photo of a yellow taxi on a street"></div>
  <div class="abs tile" style="left:335px;top:277px;width:250px;height:244px;background:linear-gradient(140deg,#b99a6e,#2f4f8a 55%,#c9a850)" role="img" aria-label="Photo of a trumpet against a blue jacket"></div>
  <div class="abs tile" style="left:335px;top:545px;width:250px;height:266px;background:linear-gradient(170deg,#d9d6cf,#6f7a58 60%,#3f4a2e)" role="img" aria-label="Photo of a lantern in a forest"></div>
  <div class="abs tile" style="left:612px;top:277px;width:247px;height:362px;background:linear-gradient(170deg,#e8b9c3,#8fc0c2 45%,#e9e4da)" role="img" aria-label="Photo of pink flowers in a jar beside an open planner"></div>
  <div class="abs tile" style="left:612px;top:666px;width:247px;height:145px;background:linear-gradient(120deg,#3a3a3a,#8a7a6a 60%,#c4a88a)" role="img" aria-label="Photo of a person holding a camera"></div>
  <div class="abs tile" style="left:883px;top:277px;width:251px;height:271px;background:linear-gradient(150deg,#e9dccb,#c9a37a 50%,#6e5844)" role="img" aria-label="Photo of a vintage radio dial"></div>
  <div class="abs tile" style="left:883px;top:545px;width:251px;height:266px;background:linear-gradient(170deg,#f0d9b4,#a7774e 50%,#4e4a52)" role="img" aria-label="Photo of friends walking outdoors at sunset"></div>
</section>

<section class="testimonial">
  <h2 class="abs center testi-title" style="font-weight:400">Testimonial</h2>
  <div class="abs avatar" role="img" aria-label="Portrait photo of the reviewer"></div>
  <p class="abs quote"><b>“</b>Morbi accumsan ipsum velit tellus aodio tincidunt auctor ornare odio sed mauris vitae consequat auctor in elit nostra per inceptos himenaeos<b>”</b></p>
  <p class="abs center quote-by">- Nora Hale</p>
  <div class="abs dots"><i></i><i class="on"></i><i></i></div>
</section>

<section class="blog">
  <div class="blog-bg" role="img" aria-label="Teal tinted photo of a desk with laptop and notebooks"></div>
  <p class="abs center eyebrow" style="top:42px">News</p>
  <h2 class="abs center heading" style="top:78px">Latest From Blog</h2>

  <article class="abs card" style="left:60px">
    <div class="card-photo" style="background:linear-gradient(160deg,#eeeeee,#c7c7c7 60%,#8a8a8a)" role="img" aria-label="Photo of a computer keyboard on a desk"></div>
    <h3 class="card-title" style="font-weight:400">Accumsan ipsum velit</h3>
    <p class="card-text">Aenean sollicitudin, lorem quis bibendum auctor nisi elit consequat ipsum nec sagittis sem nibh id elit lorem quis bendum auctor nisi elit consequat ipsum sed lorem elit.</p>
    <a class="card-more">READ MORE</a>
    <span class="card-count"><svg width="16" height="14" viewBox="0 0 16 14"><path d="M1 1h14v9H6l-4 3v-3H1z" fill="#999"/></svg>09</span>
  </article>

  <article class="abs card" style="left:428px">
    <div class="card-photo" style="background:linear-gradient(150deg,#e9e9e9,#6f7c8a 55%,#2e3a44)" role="img" aria-label="Photo of a computer mouse and keyboard"></div>
    <h3 class="card-title" style="font-weight:400">Accumsan ipsum velit</h3>
    <p class="card-text">Aenean sollicitudin, lorem quis bibendum auctor nisi elit consequat ipsum nec sagittis sem nibh id elit lorem quis bendum auctor nisi elit consequat ipsum sed lorem elit.</p>
    <a class="card-more">READ MORE</a>
    <span class="card-count"><svg width="16" height="14" viewBox="0 0 16 14"><path d="M1 1h14v9H6l-4 3v-3H1z" fill="#999"/></svg>09</span>
  </article>

  <article class="abs card" style="left:796px">
    <div class="card-photo" style="background:linear-gradient(150deg,#f1ece2,#d9c7a8 55%,#a88a62)" role="img" aria-label="Photo of an open ring binder planner"></div>
    <h3 class="card-title" style="font-weight:400">Accumsan ipsum velit</h3>
    <p class="card-text">Aenean sollicitudin, lorem quis bibendum auctor nisi elit consequat ipsum nec sagittis sem nibh id elit lorem quis bendum auctor nisi elit consequat ipsum sed lorem elit.</p>
    <a class="card-more">READ MORE</a>
    <span class="card-count"><svg width="16" height="14" viewBox="0 0 16 14"><path d="M1 1h14v9H6l-4 3v-3H1z" fill="#999"/></svg>09</span>
  </article>
</section>

<section class="contact">
  <h2 class="abs contact-title" style="font-weight:600">Contact</h2>
  <div class="abs field" style="left:69px;top:118px;width:329px;height:51px">Your Name*</div>
  <div class="abs field" style="left:431px;top:118px;width:329px;height:51px">Your Email*</div>
  <div class="abs field" style="left:69px;top:202px;width:691px;height:151px">Your Massage*</div>
  <a class="abs btn submit">Submit</a>

  <div class="abs" style="left:793px;top:115px">
    <span class="info-label"><svg width="14" height="16" viewBox="0 0 14 16"><path d="M7 0a6 6 0 0 0-6 6c0 4.5 6 10 6 10s6-5.5 6-10a6 6 0 0 0-6-6zm0 8.5A2.5 2.5 0 1 1 7 3.5a2.5 2.5 0 0 1 0 5z" fill="#222"/></svg>Location</span>
    <p class="info-text" style="margin-top:10px">B14, Harbor View Lofts, Linden Road,<br>Maple Vale, England - MV3 2KL.</p>
  </div>
  <div class="abs" style="left:793px;top:241px">
    <span class="info-label"><svg width="16" height="12" viewBox="0 0 16 12"><rect x="0" y="0" width="16" height="12" fill="#222"/><path d="M1 1l7 6 7-6" stroke="#fff" stroke-width="1.4" fill="none"/></svg>Email</span>
    <p class="info-text" style="margin-top:10px">hello@brightpathway.example</p>
  </div>
  <div class="abs" style="left:793px;top:338px">
    <span class="info-label"><svg width="14" height="14" viewBox="0 0 14 14"><path d="M3 0l3 3-1.8 1.8a8 8 0 0 0 5 5L11 8l3 3-2 3C6 14 0 8 0 2z" fill="#222"/></svg>Phone</span>
    <p class="info-text" style="margin-top:10px">+880 1700 004127</p>
  </div>
</section>

<footer class="footer">
  <nav class="abs foot-nav"><span>Home</span><span>Who I am</span><span>Services</span><span>Gallery</span><span>Blog</span><span>Contact</span></nav>
  <div class="abs socials"><i></i><i></i><i></i><i></i><i></i><i></i></div>
  <p class="abs center copy">© 20017 | All Rights Reserved.</p>
</footer>

</body>
</html>
```